Business Card Design

- one on one personal training
- group personal training
- indoor or outdoor training available
- fitness and health assessments
- personalised fitness programs
- flexible hours for training

I am a Personal Trainer in Perth Australia. I am looking to expand my word of mouth client base.

I would like to see something that uses the colours blue, green and/or yellow.

The final design should reflect the way that I train clients, fun, motivating and perhaps a little quirky?
Updates

update with a logo with the letters MPT thank you

Hi all, Have had some great designs so far. Have decided to go double sided, perhaps to use the back to list my services. Thank you

Please check update brief. Thank you.

Target Market(s)

Professionals, ages 30 to 60

Industry/Entity Type

Training

Contact Information for Business Card

Mandy Whitlock
Personal Trainer

0471 208 514
mandypersonaltrainer@fitmailbox.example
http://www.mandypersonaltrainer.example

Requirements
Must have
• A logo with the letter MPT
Nice to have
• a logo to represent either; fitness, health, change, overall well-being.
Should not have
• Please no weights or lotus flowers!!

```html
<!DOCTYPE html>
<html lang="en">
<head>
<meta charset="utf-8">
<title>Mandy Whitlock – Personal Trainer Business Card</title>
<link rel="stylesheet" href="https://fonts.googleapis.com/css2?family=Roboto+Condensed:wght@700&family=Source+Sans+3:wght@400;600&display=swap">
<style>
  :root {
    --card-bg: #ffffff;
    --ink: #1a1a1a;
    --ink-soft: #222222;
    --teal: #0f9e8f;
    --orange: #f39a2e;
    --yellow: #f5cc00;
    --green: #8cc21f;
    --blue: #1f7fc4;
    --ornament-start: #eaf3d6;
    --ornament-end: #dcebf6;
  }
  * { margin: 0; padding: 0; box-sizing: border-box; }
  html, body {
    width: 1200px;
    height: 824px;
    overflow: hidden;
    background: var(--card-bg);
  }
  .card {
    position: relative;
    width: 1200px;
    height: 824px;
    background: var(--card-bg);
    font-family: "Source Sans 3", "Myriad Pro", sans-serif;
    color: var(--ink-soft);
  }
  .ornament {
    position: absolute;
    top: 112px;
    height: 92px;
    width: 460px;
    background: linear-gradient(90deg, var(--ornament-start), var(--ornament-end));
  }
  .ornament--left { left: 28px; }
  .ornament--right { right: 28px; }
  .brand {
    position: absolute;
    top: 112px;
    left: 488px;
    width: 224px;
    text-align: center;
    font-weight: 600;
    font-size: 60px;
    line-height: 92px;
    color: var(--ink);
    letter-spacing: 2px;
  }
  .identity {
    position: absolute;
    top: 300px;
    left: 0;
    width: 1200px;
    text-align: center;
  }
  .identity__name {
    font-family: "Roboto Condensed", "Arial Narrow", sans-serif;
    font-weight: 700;
    font-size: 66px;
    line-height: 80px;
    color: var(--ink);
    letter-spacing: -0.5px;
  }
  .identity__role {
    font-size: 32px;
    line-height: 40px;
    color: var(--ink-soft);
  }
  .contact {
    position: absolute;
    left: 76px;
    top: 612px;
    list-style: none;
    font-size: 23px;
    line-height: 45px;
  }
  .services {
    position: absolute;
    left: 632px;
    top: 506px;
    list-style: none;
    font-size: 29px;
    line-height: 47px;
  }
  .services__item {
    display: flex;
    align-items: center;
  }
  .services__dot {
    width: 20px;
    height: 20px;
    border-radius: 50%;
    margin-right: 22px;
    flex: none;
  }
  .services__dot--teal { background: var(--teal); }
  .services__dot--orange { background: var(--orange); }
  .services__dot--yellow { background: var(--yellow); }
  .services__dot--green { background: var(--green); }
  .services__dot--blue { background: var(--blue); }
</style>
</head>
<body>
  <main class="card">
    <div class="ornament ornament--left" role="img" aria-label="Decorative flowing ribbon in yellow, green, red and blue"></div>
    <div class="ornament ornament--right" role="img" aria-label="Decorative flowing ribbon in yellow, green, red and blue"></div>
    <div class="brand">MPT</div>

    <header class="identity">
      <h1 class="identity__name">Mandy Whitlock</h1>
      <p class="identity__role">Personal Trainer</p>
    </header>

    <ul class="contact">
      <li class="contact__item">Phone : 0471 208 514</li>
      <li class="contact__item">E-mail: mandypersonaltrainer@fitmailbox.example</li>
      <li class="contact__item">Website: www.mandypersonaltrainer.example</li>
    </ul>

    <ul class="services">
      <li class="services__item"><span class="services__dot services__dot--teal"></span>One on one personal training</li>
      <li class="services__item"><span class="services__dot services__dot--orange"></span>Group personal training</li>
      <li class="services__item"><span class="services__dot services__dot--yellow"></span>Indoor or outdoor training available</li>
      <li class="services__item"><span class="services__dot services__dot--green"></span>Fitness and health assessments</li>
      <li class="services__item"><span class="services__dot services__dot--blue"></span>Personalised fitness programs</li>
    </ul>
  </main>
</body>
</html>
```